Label Design for Cook Marsh Kimchi Sauce – Modern Korean Fermentation Brand

We are developing the primary packaging identity for COOK MARSH, beginning with our flagship Korean Kimchi Sauce.
Cook Marsh is a contemporary Korean food brand built around an idea that is central to Korean cuisine: Tradition refined through modern food science. Our kimchi sauce is not intended to be simply another spicy Korean condiment, but rooted in authentic Korean kimchi fermentation and combines traditional fermentation knowledge with modern process control to create a consistent, flavorful and convenient shelf-stable sauce.
The goal of this project is to create a distinctive, typography-led master label and visual identity that can eventually expand across an entire Cook Marsh product family. The winning design should feel credible as the beginning of a serious international food brand, rather than as a one-off sauce label.
This first project is for our Kimchi Sauce bottle and Kimchi Paste package, but the design should establish a master brand system that can later expand into additional products such as Korean Kimchi Sauce and Korean Kimchi Paste.
Primary sauce bottle is approximately:
300 mL / 10.1 FL OZ
The label design should be developed specifically with the proportions, readability and shelf presence of a 300 mL sauce bottle in mind.
We want the design to place much greater emphasis on text, font, typography and brand hierarchy than on graphics or illustration. Should be driven primarily by distinctive typography, strong font selection or custom lettering, clear hierarchy, strong use of scale and proportion, memorable wordmark treatment, spacing and composition, recognizable label structure, with Cook Marsh and Kimchi Sauce as the visual focus. Graphics and illustrations can be used, but they should be secondary and restrained, not the main feature of the package.
A brand such as Verluna, particularly its 300 mL bottle presentation, is useful as a general reference for the importance of typography, simplicity, hierarchy, shelf recognition and longevity. We are not looking to copy Verluna's design, but we appreciate how strongly the brand is communicated through text and label structure rather than decorative graphics.
The brand concept combines:
• Korean fermentation heritage
• modern scientific precision
• real food / plant-forward ingredients
• global culinary versatility
Front Label Priorities
The front label should clearly communicate:
1. COOK MARSH as the master brand
2. KIMCHI SAUCE as the product
3. 300 mL / 10.1 FL OZ
4. A premium, clean and modern aesthetic
5. An appetizing and confident Korean identity
Possible supporting themes or optional secondary messaging:
• Authentically Fermented
• Crafted for Consistency
• Korean Chili Blend
• Bold & Tangy
• Tradition Refined by Science
These are secondary messages only. We prefer strong typography and hierarchy over excessive front-label copy. We are open to creative exploration, but the design should feel typography-led, modern, premium, bold, clean, warm, appetizing, rooted in Korean heritage, recognizable from a distance, scalable across future products
Please keep graphics minimal and secondary.
Ingredient illustrations such as cabbage, chili peppers, garlic or herbs may be used if they support the design, but they should not dominate the label.
Our preliminary concepts use more ingredient illustration than we ultimately want. We are sharing them as a starting point, but we would like designers to move the brand toward a cleaner, stronger and more typography-focused identity.
A strong concept should still work even if most decorative graphics were removed.
Please avoid:
• illustration-heavy labels
• overly busy ingredient graphics
• overly rustic packaging
• typography that feels generic or secondary
• copycat designs of existing trendy sauce brands
The final design should make the consumer remember COOK MARSH, not simply the pictures on the bottle.

```html
<!DOCTYPE html>
<html lang="en">
<head>
<meta charset="utf-8">
<title>Cook Marsh Kimchi Sauce Label</title>
<link rel="stylesheet" href="https://fonts.googleapis.com/css2?family=Barlow:wght@400;500;800&family=Nanum+Myeongjo:wght@700&family=Oswald:wght@600&family=Poppins:wght@400;600&display=swap">
<style>
  :root {
    --bg: #dcdcdc;
    --red: #d71f28;
    --ink: #0b0b0c;
    --cream: #faf6ee;
    --tan: #d8c09a;
    --white: #ffffff;
  }
  html, body {
    margin: 0;
    padding: 0;
    width: 1200px;
    height: 970px;
    overflow: hidden;
    background: var(--bg);
  }
  .canvas {
    position: relative;
    width: 1200px;
    height: 970px;
  }
  .label {
    position: absolute;
    left: 259px;
    top: 35px;
    width: 681px;
    height: 900px;
  }
  .label-outer { fill: var(--red); }
  .label-inner { fill: var(--cream); stroke: var(--ink); stroke-width: 10; }
  .brand-name {
    font-family: "Oswald", sans-serif;
    font-weight: 600;
    font-size: 112px;
    fill: var(--red);
    letter-spacing: 2px;
  }
  .divider { stroke: var(--tan); stroke-width: 2; }
  .descriptor {
    font-family: "Poppins", sans-serif;
    font-weight: 400;
    font-size: 40px;
    fill: var(--tan);
  }
  .product-name {
    font-family: "Barlow", sans-serif;
    font-weight: 800;
    font-size: 142px;
    fill: var(--ink);
    letter-spacing: -2px;
  }
  .korean-name {
    font-family: "Nanum Myeongjo", serif;
    font-weight: 700;
    font-size: 96px;
    fill: var(--red);
  }
  .ingredient-art { fill: var(--tan); opacity: 0.45; }
  .claim-pill { fill: var(--red); }
  .claim-text {
    font-family: "Barlow", sans-serif;
    font-weight: 500;
    font-size: 31px;
    fill: var(--white);
  }
  .tagline {
    font-family: "Poppins", sans-serif;
    font-weight: 600;
    font-size: 26px;
    fill: var(--red);
  }
  .volume {
    font-family: "Barlow", sans-serif;
    font-weight: 400;
    font-size: 29px;
    fill: var(--ink);
  }
</style>
</head>
<body>
<div class="canvas">
  <svg class="label" viewBox="0 0 795 1050" xmlns="http://www.w3.org/2000/svg">
    <defs>
      <path id="label-shape" d="M398,0 C490,0 560,55 585,140 C600,190 640,205 710,205 L712,470 C715,520 745,540 790,550 L795,880 C795,960 745,1000 680,1000 L575,1000 C550,1000 540,1010 540,1025 L540,1035 C540,1045 532,1050 522,1050 L273,1050 C263,1050 255,1045 255,1035 L255,1025 C255,1010 245,1000 220,1000 L115,1000 C50,1000 0,960 0,880 L5,550 C50,540 80,520 83,470 L85,205 C155,205 195,190 210,140 C235,55 305,0 398,0 Z"/>
    </defs>
    <use href="#label-shape" class="label-outer"/>
    <use href="#label-shape" class="label-inner" transform="translate(23.85,31.5) scale(0.94)"/>

    <text class="brand-name" x="397.5" y="265" text-anchor="middle">COOK</text>
    <text class="brand-name" x="397.5" y="362" text-anchor="middle">MARSH</text>

    <line class="divider" x1="268" y1="380" x2="527" y2="380"/>
    <text class="descriptor" x="397.5" y="430" text-anchor="middle">Korean Chili Blend</text>

    <text class="product-name" x="397.5" y="553" text-anchor="middle">KIMCHI</text>
    <text class="product-name" x="397.5" y="660" text-anchor="middle">SAUCE</text>

    <path class="ingredient-art" role="img" aria-label="Line drawing of a cabbage wedge" d="M92,680 C140,680 215,700 245,735 C230,770 200,790 160,788 C120,782 95,740 92,680 Z"/>
    <path class="ingredient-art" role="img" aria-label="Line drawing of a cabbage wedge" d="M655,645 C690,680 682,750 650,785 L572,788 C590,740 615,680 655,645 Z"/>

    <text class="korean-name" x="397.5" y="775" text-anchor="middle">쿡마시</text>

    <rect class="claim-pill" x="178" y="819" width="444" height="38" rx="19"/>
    <text class="claim-text" x="397.5" y="849" text-anchor="middle">Authentically Fermented</text>

    <text class="tagline" x="397.5" y="902" text-anchor="middle">Tradition Refined by Science</text>
    <text class="volume" x="397.5" y="950" text-anchor="middle">300 mL / 10.1 FL OZ</text>
  </svg>
</div>
</body>
</html>
```